Business Card Design

I need a business card for company that is a limited company that was originally an off-road vehicle company (atv's side by sides snowmobiles and motorcycles) and I have recently sold the assets of the company that was operating under a different name and have become semi retired. I continue to do maintenance on these types of vehicles and also sell and install parts and accessories. Recently I have also contracted to a snowmobile club to operate their groomer to groom the snowmobile trails. I would like bright and bold colors.
Industry/Entity Type
Club
Contact Information for Business Card
KWT Holdings Ltd.
Marcus Ellery
780-555-0143

```html
<!DOCTYPE html>
<html lang="en">
<head>
<meta charset="utf-8">
<title>KWT Holdings Ltd. – Business Card</title>
<link rel="stylesheet" href="https://fonts.googleapis.com/css2?family=Arimo:wght@400;700&display=swap">
<style>
  :root {
    --backdrop: #d9d9d9;
    --card-orange: #f0522a;
    --card-yellow: #fde01f;
    --photo-dark: #3a120a;
    --photo-mid: #b8321a;
    --ink-black: #111111;
    --ink-white: #ffffff;
    --card-w: 900px;
    --card-h: 514px;
  }
  * { box-sizing: border-box; margin: 0; padding: 0; }
  html, body {
    width: 1179px;
    height: 1200px;
    overflow: hidden;
    background: var(--backdrop);
    font-family: "Arimo", Arial, sans-serif;
  }
  .stage {
    position: relative;
    width: 1179px;
    height: 1200px;
  }
  .card {
    position: absolute;
    left: 140px;
    width: var(--card-w);
    height: var(--card-h);
    background: var(--card-orange);
    overflow: hidden;
    box-shadow: 0 6px 18px rgba(0,0,0,0.18);
  }
  .card--front { top: 40px; }
  .card--back { top: 620px; }
  .card__art {
    position: absolute;
    inset: 0;
    width: 100%;
    height: 100%;
  }
  .company-name {
    position: absolute;
    left: 480px;
    top: 150px;
    width: 400px;
    color: var(--card-yellow);
    font-weight: 700;
    font-size: 62px;
    line-height: 1.05;
    letter-spacing: 0.5px;
  }
  .contact {
    position: absolute;
    left: 360px;
    top: 52px;
    color: var(--ink-white);
  }
  .contact__phone {
    font-weight: 700;
    font-size: 36px;
    letter-spacing: 0.5px;
  }
  .contact__email {
    font-weight: 400;
    font-size: 27px;
    margin-top: 2px;
  }
  .person {
    position: absolute;
    left: 44px;
    top: 150px;
    color: var(--ink-black);
  }
  .person__name {
    font-weight: 700;
    font-size: 35px;
    margin-bottom: 14px;
  }
  .credentials {
    list-style: none;
    font-size: 29px;
    line-height: 1.08;
    padding-left: 18px;
  }
  .credentials li {
    position: relative;
    padding-left: 16px;
    margin-bottom: 4px;
  }
  .credentials li::before {
    content: "";
    position: absolute;
    left: 0;
    top: 12px;
    width: 8px;
    height: 8px;
    background: var(--ink-black);
  }
</style>
</head>
<body>
<main class="stage">

  <section class="card card--front" aria-label="Business card front">
    <svg class="card__art" viewBox="0 0 900 514" aria-hidden="false">
      <defs>
        <linearGradient id="frontPhotoTone" x1="0" y1="0" x2="1" y2="1">
          <stop offset="0" stop-color="#5a1a0c"/>
          <stop offset="0.45" stop-color="#b8321a"/>
          <stop offset="1" stop-color="#e24a24"/>
        </linearGradient>
      </defs>
      <polygon role="img" aria-label="Photo of an off-road vehicle tire and red wheel hub"
               points="0,0 560,0 560,150 0,330"
               fill="url(#frontPhotoTone)"/>
    </svg>
    <p class="company-name">KWT Holdings Ltd.</p>
  </section>

  <section class="card card--back" aria-label="Business card back">
    <svg class="card__art" viewBox="0 0 900 514">
      <defs>
        <radialGradient id="backPhotoTone" cx="0.85" cy="0.7" r="0.6">
          <stop offset="0" stop-color="#3a120a"/>
          <stop offset="0.5" stop-color="#a02c16"/>
          <stop offset="1" stop-color="#f0522a" stop-opacity="0"/>
        </radialGradient>
      </defs>
      <rect role="img" aria-label="Photo of an off-road vehicle tire on a red wheel"
            x="380" y="120" width="520" height="394" fill="url(#backPhotoTone)"/>
      <polygon class="card__yellow-band" points="0,0 200,0 900,470 900,514 0,514" fill="#fde01f"/>
    </svg>

    <div class="contact">
      <p class="contact__phone">780-555-0143</p>
      <p class="contact__email">kwtholdings.77@example.com</p>
    </div>

    <div class="person">
      <p class="person__name">Marcus Ellery</p>
      <ul class="credentials">
        <li>journeyman red seal<br>automotive technician</li>
        <li>journeyman red seal<br>motorcycle technician</li>
        <li>journeyman parts man</li>
      </ul>
    </div>
  </section>

</main>
</body>
</html>
```